Email Newsletter Header/Banner

We are an Australian Real Estate investment company that require a header for our email newsletter. Dimensions 790px by 180px.

Header must include both our website logos
http://www.kelvorplan.com.au
http://kelvorhomes.com.au

We want the header to have a human or community feel. No corporate or business look. Clean modern design
Updates

Please only use the logo of Kelvor PlanĀ http://www.kelvorplan.com.au

Target Market(s)

Real Estate Investors

Industry/Entity Type

Investment

Requirements
Must have
• Community or human feel

```html
<!DOCTYPE html>
<html lang="en">
<head>
<meta charset="utf-8">
<title>Kelvor Plan Newsletter Header</title>
<link href="https://fonts.googleapis.com/css2?family=Open+Sans:wght@600&family=Questrial&display=swap" rel="stylesheet">
<style>
  :root {
    --page-bg: #ebebeb;
    --banner-bg: #ffffff;
    --ink: #1f1f1f;
    --brand-blue: #3a8fd0;
    --brand-red: #c1002b;
    --band-red: #c0062c;
    --band-text: #ffffff;
    --crowd-skin: #d8b79a;
    --crowd-navy: #3d4a5e;
    --crowd-khaki: #b7a27a;
    --crowd-teal: #7fb2b5;
    --crowd-yellow: #e2c23a;
    --crowd-light: #f4f1ec;
  }
  html, body {
    margin: 0;
    width: 1200px;
    height: 368px;
    overflow: hidden;
    background: var(--page-bg);
  }
  .newsletter-header {
    position: absolute;
    left: 61px;
    top: 61px;
    width: 1078px;
    height: 246px;
    background: var(--banner-bg);
  }
  .site-name {
    position: absolute;
    display: flex;
    align-items: center;
    gap: 14px;
    margin: 0;
    font-family: "Open Sans", Arial, sans-serif;
    font-weight: 600;
    font-size: 46px;
    line-height: 1;
    letter-spacing: -0.6px;
    color: var(--ink);
  }
  .site-name__mark {
    width: 30px;
    height: 30px;
    flex: none;
  }
  .site-name--plan { left: 116px; top: 66px; }
  .site-name--plan .site-name__mark { background: var(--brand-blue); }
  .site-name--homes { left: 24px; top: 124px; }
  .site-name--homes .site-name__mark { background: var(--brand-red); }
  .community-photo {
    position: absolute;
    left: 532px;
    top: 58px;
    width: 526px;
    height: 118px;
    background:
      linear-gradient(180deg, var(--crowd-light) 0%, rgba(244,241,236,0) 30%, rgba(244,241,236,0) 85%, var(--crowd-light) 100%),
      linear-gradient(90deg, var(--crowd-khaki), var(--crowd-navy) 14%, var(--crowd-skin) 28%, var(--crowd-teal) 42%, var(--crowd-skin) 56%, var(--crowd-navy) 70%, var(--crowd-skin) 84%, var(--crowd-yellow));
    opacity: 0.8;
  }
  .address-band {
    position: absolute;
    left: 0;
    bottom: 0;
    width: 100%;
    height: 48px;
    background: var(--band-red);
    display: flex;
    align-items: center;
    justify-content: center;
    font-family: "Questrial", "Century Gothic", sans-serif;
    font-style: normal;
    font-size: 31px;
    letter-spacing: 1.2px;
    color: var(--band-text);
  }
</style>
</head>
<body>
  <header class="newsletter-header">
    <p class="site-name site-name--plan"><span class="site-name__mark"></span>kelvorplan.com</p>
    <p class="site-name site-name--homes"><span class="site-name__mark"></span>kelvorhomes.com</p>
    <div class="community-photo" role="img" aria-label="A friendly community line-up of diverse people from many walks of life: tradespeople, nurses, office workers and families standing side by side"></div>
    <address class="address-band">PO Box K2240, Harbour Exchange, NSW 2000</address>
  </header>
</body>
</html>
```